Coin collector banner ad for specialty insurance

We need a logo designed banner ad (multiple ads) to align with the coin collector market while incorporating color palette logo and call to action. Color palette of Fernholt. Dimension, images, example designs and color palette attached. The context should include 'Specialty Insurance for your coin collection' please refer to the designed examples

Target Market(s)

Coin collectors 30-65+ years of age primarily male

Industry/Entity Type

Insurance

Font styles to use
Sans Serif

Requirements
Must have
• color palette, logo, word mark, Call to Action, The words 'Specialty Insurance for your coin collection'
Nice to have
• Call to actions
Should not have
• ba

```html
<!DOCTYPE html>
<html lang="en">
<head>
<meta charset="utf-8">
<title>Fernholt coin collection insurance banners</title>
<link href="https://fonts.googleapis.com/css2?family=Montserrat:wght@300;400;600;700&display=swap" rel="stylesheet">
<style>
  :root {
    --page: #f2f2f2;
    --blue: #1aa3de;
    --blue-deep: #0d63a5;
    --blue-mid: #1380c4;
    --sky: #9fd2ee;
    --ink: #1b1b1b;
    --gold: #b58d2c;
    --gold-light: #e6c65c;
    --silver: #d9dde0;
    --silver-dark: #8d9398;
    --white: #ffffff;
  }
  * { margin: 0; padding: 0; box-sizing: border-box; }
  html, body { width: 1200px; height: 960px; overflow: hidden; }
  body {
    background: var(--page);
    font-family: "Montserrat", Arial, sans-serif;
    position: relative;
  }
  .banner {
    position: absolute;
    left: 83px;
    width: 1035px;
    height: 284px;
    overflow: hidden;
    background: linear-gradient(180deg, var(--white) 0%, var(--white) 45%, #d5ebf8 78%, var(--sky) 100%);
    box-shadow: 0 8px 10px rgba(0,0,0,0.35);
  }
  .banner--top { top: 142px; }
  .banner--bottom { top: 500px; }
  .facets { position: absolute; inset: 0; }
  .coin-ring {
    position: absolute;
    border-radius: 50%;
    background: linear-gradient(180deg, var(--blue) 0%, var(--blue-deep) 100%);
  }
  .coin-ring--silver { left: 142px; top: 20px; width: 260px; height: 260px; }
  .coin-ring--gold { left: -11px; top: 6px; width: 204px; height: 204px; }
  .coin { position: absolute; border-radius: 50%; }
  .coin--silver {
    left: 173px; top: 51px; width: 198px; height: 198px;
    background: radial-gradient(circle at 35% 40%, var(--white) 0%, var(--silver) 45%, var(--silver-dark) 75%, #1a1a1a 100%);
  }
  .coin--gold {
    left: -3px; top: 14px; width: 188px; height: 188px;
    background: var(--white);
  }
  .coin--gold-face {
    left: 0px; top: 17px; width: 182px; height: 182px;
    background: radial-gradient(circle at 45% 45%, var(--gold-light) 0%, var(--gold) 70%, #6e5216 100%);
  }
  .learn-more {
    position: absolute;
    left: 0; top: 232px;
    width: 185px; height: 33px;
    background: linear-gradient(180deg, var(--blue-mid), var(--blue-deep));
    clip-path: polygon(0 0, 84% 0, 100% 100%, 0 100%);
    color: var(--white);
    font-size: 19px;
    font-weight: 300;
    line-height: 33px;
    padding-left: 9px;
    letter-spacing: -0.2px;
  }
  .learn-more strong { font-weight: 600; }
  .brand {
    position: absolute;
    right: 38px; top: 15px;
    display: flex; align-items: center; gap: 12px;
  }
  .brand-square { width: 48px; height: 48px; background: var(--blue); }
  .brand-name { font-size: 24px; font-weight: 700; color: var(--ink); letter-spacing: -0.2px; }
  .headline { text-transform: uppercase; }
  .headline-main,
  .headline-sub {
    position: absolute;
    right: 36px;
    white-space: nowrap;
    line-height: 1;
  }
  .headline-main {
    top: 75px;
    font-size: 46px; font-weight: 700;
    color: var(--blue);
    letter-spacing: 0.6px;
  }
  .headline-sub {
    top: 126px;
    font-size: 37px; font-weight: 300;
    color: var(--ink);
    letter-spacing: 0.6px;
  }
  .byline {
    position: absolute;
    left: 564px; width: 300px; top: 172px;
    text-align: center;
    font-size: 26px; font-weight: 300;
    line-height: 1.2;
    color: var(--blue);
    letter-spacing: 0.8px;
  }
  .cta {
    position: absolute;
    left: 623px; top: 224px;
    width: 184px; height: 35px;
    border-radius: 4px;
    background: linear-gradient(180deg, var(--blue) 0%, var(--blue-mid) 55%, var(--blue-deep) 100%);
    color: var(--white);
    display: flex; align-items: center;
    overflow: hidden;
  }
  .cta-label { flex: 1; font-size: 17px; font-weight: 300; padding-left: 6px; letter-spacing: 0.8px; color: #d8f0ff; white-space: nowrap; }
  .cta-label strong { font-weight: 700; color: #0b2f4e; }
  .cta-arrow {
    width: 31px; height: 100%;
    border-left: 1px solid rgba(255,255,255,0.6);
    display: flex; align-items: center; justify-content: center;
    background: var(--blue-deep);
  }
</style>
</head>
<body>

<section class="banner banner--top">
  <svg class="facets" width="1035" height="284" viewBox="0 0 1035 284" aria-hidden="true">
    <polygon points="500,180 1035,120 1035,284 600,284" fill="#ffffff" opacity="0.25"/>
    <polygon points="505,230 650,190 650,284 505,284" fill="#ffffff" opacity="0.18"/>
    <polygon points="840,284 1035,210 1035,284" fill="#7cc2e8" opacity="0.35"/>
  </svg>
  <div class="coin-ring coin-ring--silver"></div>
  <div class="coin coin--silver" role="img" aria-label="Silver proof coin"></div>
  <div class="coin-ring coin-ring--gold"></div>
  <div class="coin coin--gold"></div>
  <div class="coin coin--gold-face" role="img" aria-label="Gold bullion coin"></div>
  <div class="learn-more">LEARN <strong>MORE</strong></div>
  <div class="brand"><span class="brand-square"></span><span class="brand-name">FERNHOLT</span></div>
  <h1 class="headline"><span class="headline-main">Specialty Insurance</span><span class="headline-sub">For your coin collection</span></h1>
  <p class="byline">by Fernholt</p>
  <div class="cta"><span class="cta-label">GET <strong>STARTED</strong></span>
    <span class="cta-arrow"><svg width="18" height="12" viewBox="0 0 18 12"><polygon points="0,0 9,6 0,12" fill="#0b2f4e"/><polygon points="9,0 18,6 9,12" fill="#0b2f4e"/></svg></span>
  </div>
</section>

<section class="banner banner--bottom">
  <svg class="facets" width="1035" height="284" viewBox="0 0 1035 284" aria-hidden="true">
    <polygon points="500,180 1035,120 1035,284 600,284" fill="#ffffff" opacity="0.25"/>
    <polygon points="505,230 650,190 650,284 505,284" fill="#ffffff" opacity="0.18"/>
    <polygon points="840,284 1035,210 1035,284" fill="#7cc2e8" opacity="0.35"/>
  </svg>
  <div class="coin-ring coin-ring--silver"></div>
  <div class="coin coin--silver" role="img" aria-label="Silver proof coin"></div>
  <div class="coin-ring coin-ring--gold"></div>
  <div class="coin coin--gold"></div>
  <div class="coin coin--gold-face" role="img" aria-label="Gold bullion coin"></div>
  <div class="learn-more">LEARN <strong>MORE</strong></div>
  <div class="brand"><span class="brand-square"></span><span class="brand-name">FERNHOLT</span></div>
  <h2 class="headline"><span class="headline-main">Specialty Insurance</span><span class="headline-sub">For your coin collection</span></h2>
  <p class="byline">by Fernholt</p>
  <div class="cta"><span class="cta-label">GET <strong>STARTED</strong></span>
    <span class="cta-arrow"><svg width="18" height="12" viewBox="0 0 18 12"><polygon points="0,0 9,6 0,12" fill="#0b2f4e"/><polygon points="9,0 18,6 9,12" fill="#0b2f4e"/></svg></span>
  </div>
</section>

</body>
</html>
```